Harbor Crest Residential Business Card Design - Logo Provided

business card design - LOGO PROVIDED. private capital fund investing in: commercial real estate (apartments), asset backed lending, private credit, flexible capital

Target Market(s)

private capital: commercial real estate (apartments), asset backed lending, private credit, flexible capital

Industry/Entity Type

alternative asset management

Contact Information for Business Card

logo, name, title, phone number, email and website

Font styles to use
Sans Serif

Colors
0054AA
0677BA
7BADD7
CADEEF
E8F1F8
EB3D1F
EC4F4E
F09395
F8D3D4
FCEDEE

Requirements
Must have
• use of logo on both sides and a qr code on the back

```html
<!DOCTYPE html>
<html lang="en">
<head>
<meta charset="UTF-8">
<title>Harbor Crest Residential – Business Card</title>
<link href="https://fonts.googleapis.com/css2?family=Poppins:wght@700;800&family=Lexend:wght@300;400;600;700&display=swap" rel="stylesheet">
<style>
  :root {
    --page-bg: #dedede;
    --brand-blue: #0054aa;
    --brand-blue-mid: #0677ba;
    --brand-blue-soft: #cadeef;
    --brand-blue-pale: #e8f1f8;
    --red: #e0100e;
    --card-light: #f5f5f5;
    --ink: #222222;
    --white: #ffffff;
  }
  * { margin: 0; padding: 0; box-sizing: border-box; }
  html, body {
    width: 1200px; height: 437px; overflow: hidden;
    background: var(--page-bg);
  }
  .canvas { position: relative; width: 1200px; height: 437px; }

  .side-label {
    position: absolute;
    font-family: "Poppins", sans-serif;
    font-weight: 800;
    font-size: 38px;
    line-height: 1;
    color: #000;
    letter-spacing: 0.5px;
  }
  .side-label--front { left: 35px; top: 30px; }
  .side-label--back { left: 619px; top: 37px; }

  .card {
    position: absolute;
    width: 548px; height: 322px;
    overflow: hidden;
  }
  .card--front { left: 35px; top: 80px; background: var(--brand-blue); }
  .card--back { left: 621px; top: 79px; background: var(--card-light); }

  .brand {
    position: absolute;
    display: flex; align-items: center;
    font-family: "Lexend", sans-serif;
    font-weight: 700;
    text-transform: uppercase;
    line-height: 1.02;
  }
  .brand__mark { flex: none; }
  .card--front .brand {
    left: 50%; top: 50%; transform: translate(-50%, -50%);
    gap: 16px; color: var(--white); font-size: 27px;
  }
  .card--front .brand__mark { width: 56px; height: 56px; background: var(--white); }
  .card--back .brand {
    left: 388px; top: 194px; gap: 8px;
    color: var(--brand-blue); font-size: 16px;
  }
  .card--back .brand__mark { width: 26px; height: 26px; background: var(--brand-blue); }

  .qr-code {
    position: absolute;
    left: 452px; top: 96px;
    width: 68px; height: 68px;
    background: var(--white);
    border: 6px solid var(--brand-blue);
    outline: 1px solid var(--brand-blue-soft);
  }
  .qr-code__field {
    width: 100%; height: 100%;
    background: var(--brand-blue-pale);
  }

  .backdrop-curves { position: absolute; inset: 0; }

  .holder {
    position: absolute; left: 0; right: 0; top: 30px;
    text-align: center;
  }
  .holder__name {
    font-family: "Poppins", sans-serif; font-weight: 700;
    font-size: 17.5px; color: var(--brand-blue); line-height: 1.3;
  }
  .holder__title {
    font-family: "Lexend", sans-serif; font-weight: 400;
    font-size: 18px; color: var(--red); margin-top: 6px; letter-spacing: 0.3px;
  }

  .contacts {
    position: absolute; left: 32px; top: 199px;
    list-style: none;
    font-family: "Lexend", sans-serif; font-weight: 300;
    font-size: 14.5px; color: var(--ink); letter-spacing: 0.45px;
  }
  .contacts__item { display: flex; align-items: center; gap: 11px; height: 27px; margin-bottom: 4.5px; }
  .contacts__icon {
    width: 27px; height: 27px; border-radius: 50%;
    display: flex; align-items: center; justify-content: center; flex: none;
  }
  .contacts__icon--blue { background: var(--brand-blue); }
  .contacts__icon--red { background: var(--red); }
</style>
</head>
<body>
<div class="canvas">
  <div class="side-label side-label--front">FRONT</div>
  <div class="side-label side-label--back">BACK</div>

  <section class="card card--front">
    <div class="brand">
      <span class="brand__mark"></span>
      <span class="brand__name">Harbor Crest<br>Residential</span>
    </div>
  </section>

  <section class="card card--back">
    <svg class="backdrop-curves" width="548" height="322" viewBox="0 0 548 322" aria-hidden="true">
      <path d="M430 0 C520 80 520 220 400 322 L548 322 L548 0 Z" fill="#fbfbfb"/>
      <path d="M480 0 C560 90 540 230 470 322" fill="none" stroke="#ececec" stroke-width="2"/>
      <path d="M330 0 C420 60 460 200 520 322" fill="none" stroke="#efefef" stroke-width="1.5"/>
    </svg>

    <div class="holder">
      <div class="holder__name">Your Name</div>
      <div class="holder__title">Director Manager</div>
    </div>

    <div class="qr-code" role="img" aria-label="QR code linking to the company website">
      <div class="qr-code__field"></div>
    </div>

    <ul class="contacts">
      <li class="contacts__item">
        <span class="contacts__icon contacts__icon--blue">
          <svg width="14" height="14" viewBox="0 0 24 24"><path fill="#fff" d="M6.6 10.8a15 15 0 0 0 6.6 6.6l2.2-2.2a1 1 0 0 1 1-.25 11.4 11.4 0 0 0 3.6.57 1 1 0 0 1 1 1V20a1 1 0 0 1-1 1A17 17 0 0 1 3 4a1 1 0 0 1 1-1h3.5a1 1 0 0 1 1 1c0 1.25.2 2.45.57 3.57a1 1 0 0 1-.25 1z"/></svg>
        </span>
        <span>123-456-7890</span>
      </li>
      <li class="contacts__item">
        <span class="contacts__icon contacts__icon--red">
          <svg width="15" height="15" viewBox="0 0 24 24" fill="none" stroke="#fff" stroke-width="1.6"><circle cx="12" cy="12" r="9"/><ellipse cx="12" cy="12" rx="4" ry="9"/><path d="M3 12h18M4.5 7.5h15M4.5 16.5h15"/></svg>
        </span>
        <span>www.yourwebsite.com</span>
      </li>
      <li class="contacts__item">
        <span class="contacts__icon contacts__icon--blue">
          <svg width="14" height="14" viewBox="0 0 24 24"><rect x="2" y="5" width="20" height="14" rx="1.5" fill="#fff"/><path d="M3 6l9 7 9-7" fill="none" stroke="#0054aa" stroke-width="1.8"/></svg>
        </span>
        <span>hello@youremail.com</span>
      </li>
    </ul>

    <div class="brand">
      <span class="brand__mark"></span>
      <span class="brand__name">Harbor Crest<br>Residential</span>
    </div>
  </section>
</div>
</body>
</html>
```